Oral Surgeon Referral Pads

Hello. We need referral pads for Dr Helena Vasquier, DDS board certified oral surgeon's new office - Cedar Hollow Oral & Maxillofacial Surgery. See logo uploaded. See some images we would like included
Updates

Designs look the same

Font styles to use
Serif
Script

Colors
00AB8E
00BBA5
67D7C9
C6EFE9
E9F9F6

Requirements
Must have
• Color Pantone 623c. Also foldable business cards

```html
<!DOCTYPE html>
<html lang="en">
<head>
<meta charset="utf-8">
<title>Cedar Hollow Oral &amp; Maxillofacial Surgery – Referral Pad</title>
<link href="https://fonts.googleapis.com/css2?family=Open+Sans:wght@400;600&family=Lora:wght@400&display=swap" rel="stylesheet">
<style>
:root{
  --stage:#616161;
  --paper:#ffffff;
  --navy:#1f2d6b;
  --ink:#2a2a2a;
  --chart-frame:#a9c9dc;
  --chart-fill:#eef3f7;
  --tissue-fill:#f1f1f1;
}
*{margin:0;padding:0;box-sizing:border-box}
html,body{width:1200px;height:1004px;overflow:hidden}
body{background:var(--stage);font-family:"Open Sans",sans-serif;color:var(--ink);position:relative}
.stage-title{position:absolute;top:38px;left:0;width:1200px;text-align:center;color:#fff;font-size:46px;font-weight:400;line-height:1}
.sheet{position:absolute;top:156px;width:507px;height:709px;background:var(--paper);box-shadow:0 4px 10px rgba(0,0,0,.35)}
.sheet-front{left:74px}
.sheet-back{left:619px}
.sheet-band{position:absolute;left:0;bottom:0;width:100%;height:16px;background:var(--navy)}
.sheet-back .sheet-band{height:12px}
.t{position:absolute;white-space:nowrap;line-height:1}
.doctor{left:22px;top:39px;font-size:15px;font-weight:600;color:var(--navy)}
.contact{left:22px;font-size:12.5px;display:flex;align-items:center;gap:5px}
.contact svg{width:10px;height:10px;fill:var(--navy)}
.practice{position:absolute;left:230px;width:265px;text-align:center;font-family:"Lora",serif;color:var(--navy);font-weight:400;line-height:1}
.practice-name{top:88px;font-size:29px}
.practice-sub{top:124px;font-size:15.5px}
.practice-dot{position:absolute;left:353px;top:150px;width:9px;height:9px;border-radius:50%;background:var(--navy)}
.field{left:22px;font-size:12px}
.rule{position:absolute;height:1.5px;background:var(--navy)}
.rule-full{left:22px;width:459px}
.heading{font-size:11px;font-weight:600}
.heading-lg{font-size:13.5px;font-weight:600}
.opt{font-size:13px;display:flex;align-items:center;gap:6px}
.opt-sm{font-size:11.5px;font-weight:600}
.box{display:inline-block;width:7.5px;height:7.5px;border:1.3px solid var(--navy);flex:none}
.intro{left:24px;top:37px;font-size:12.5px}
.tooth-chart{position:absolute;left:19px;top:79px;width:249px;height:130px;background:var(--chart-fill);border:2px solid var(--chart-frame)}
.tissue-chart{position:absolute;left:295px;top:75px;width:180px;height:145px;background:var(--tissue-fill);border-radius:50% 50% 45% 45%}
.instructions{position:absolute;left:23px;width:470px;font-size:10.2px;font-weight:600;line-height:15.5px;color:#333}
.instructions-title{position:absolute;left:23px;top:262px;font-size:10.5px;font-weight:600;color:#333}
</style>
</head>
<body>
<div class="stage-title">Change 03</div>

<section class="sheet sheet-front">
  <div class="t doctor">Dr Helena Vasquier</div>
  <div class="t contact" style="top:83px"><svg viewBox="0 0 10 10"><path d="M5 0a3.6 3.6 0 0 0-3.6 3.6C1.4 6.3 5 10 5 10s3.6-3.7 3.6-6.4A3.6 3.6 0 0 0 5 0zm0 5.2a1.6 1.6 0 1 1 0-3.2 1.6 1.6 0 0 1 0 3.2z"/></svg>Your address, City State, Zip 1234</div>
  <div class="t contact" style="top:101px"><svg viewBox="0 0 10 10"><path d="M2.2 0.6 3.8 2.6 2.9 3.7c.7 1.4 1.9 2.6 3.4 3.4l1.1-.9 2 1.6-.9 1.6C4.4 9.3.7 5.6.6 1.5z"/></svg>123 456 789</div>
  <div class="t contact" style="top:119px"><svg viewBox="0 0 10 10"><path d="M2 0h5v3H2zM0 3.5h10V10H0zm2 2h1.5V7H2zm3 0h1.5V7H5zm-3 2h1.5V9H2zm3 0h1.5V9H5z"/></svg>123 456 789</div>
  <div class="t contact" style="top:137px"><svg viewBox="0 0 10 10"><path d="M0 2h10v7H0zm1 1 4 3 4-3v-.2H1z"/></svg>info@cedarhollowsurgery.com</div>

  <div class="practice practice-name">Cedar Hollow</div>
  <div class="practice practice-sub">Oral &amp; Maxillofacial Surgery</div>
  <span class="practice-dot"></span>

  <div class="t field" style="top:180px">Today’ s Date &nbsp; DD &nbsp;&nbsp;&nbsp; / &nbsp;&nbsp;&nbsp;&nbsp; MM &nbsp;&nbsp; / &nbsp;&nbsp; YYY</div>
  <div class="rule rule-full" style="top:203px"></div>
  <div class="t field" style="top:215px">Patient’ s Name</div>
  <div class="rule rule-full" style="top:236px"></div>
  <div class="t field" style="top:247px">Patient’ Phone Number</div>
  <div class="rule rule-full" style="top:268px"></div>
  <div class="t field" style="top:276px">Referred by</div>
  <div class="rule rule-full" style="top:296px"></div>
  <div class="t field" style="top:308px;left:23px">Additional Comments</div>

  <div class="t heading" style="left:60px;top:347px">PROCEDURE</div>
  <div class="t opt opt-sm" style="left:60px;top:367px"><span class="box"></span>Extraction</div>
  <div class="t opt opt-sm" style="left:145px;top:366px"><span class="box"></span>Implants</div>
  <div class="t opt opt-sm" style="left:231px;top:367px"><span class="box"></span>Consultation</div>
  <div class="t opt opt-sm" style="left:323px;top:366px"><span class="box"></span>Radiogrphs</div>

  <div class="t opt" style="left:22px;top:402px"><span class="box"></span>Wisdom Teeth</div>
  <div class="t opt" style="left:22px;top:420px"><span class="box"></span>Extraction</div>
  <div class="t opt" style="left:22px;top:438px"><span class="box"></span>Implants</div>
  <div class="t opt" style="left:22px;top:456px"><span class="box"></span>Bone Grafing</div>
  <div class="t opt" style="left:22px;top:474px"><span class="box"></span>Exposure and bonding</div>
  <div class="t opt" style="left:22px;top:492px"><span class="box"></span>Biopsy(SOFT or Hard Tissue)</div>

  <div class="t opt" style="left:229px;top:402px"><span class="box"></span>Lesion Evaluation</div>
  <div class="t opt" style="left:229px;top:420px"><span class="box"></span>Infection (I&amp;D</div>
  <div class="t opt" style="left:229px;top:438px"><span class="box"></span>Alveoloplasty</div>
  <div class="t opt" style="left:229px;top:456px"><span class="box"></span>Frenectomy</div>
  <div class="t opt" style="left:229px;top:474px"><span class="box"></span>Orthognathic</div>
  <div class="t opt" style="left:229px;top:492px"><span class="box"></span>TMJ</div>
  <div class="t opt" style="left:229px;top:510px"><span class="box"></span>Other</div>
  <div class="rule" style="left:244px;top:530px;width:70px"></div>
  <div class="rule" style="left:244px;top:549px;width:70px"></div>

  <div class="t opt" style="left:356px;top:402px">Implants</div>
  <div class="t opt" style="left:349px;top:419px"><span class="box"></span>Alderfix</div>
  <div class="t opt" style="left:349px;top:437px"><span class="box"></span>OsteoLine</div>
  <div class="t opt" style="left:349px;top:455px"><span class="box"></span>Other</div>
  <div class="rule" style="left:363px;top:478px;width:70px"></div>
  <div class="rule" style="left:363px;top:497px;width:70px"></div>

  <div class="t heading-lg" style="left:60px;top:558px">Surgical Template</div>
  <div class="t opt" style="left:22px;top:578px"><span class="box"></span>To be provided by Restorative dentist</div>
  <div class="t opt" style="left:286px;top:578px"><span class="box"></span>To be fabricated by the surgeon</div>
  <div class="t opt" style="left:22px;top:596px"><span class="box"></span>Other</div>
  <div class="rule" style="left:91px;top:606px;width:170px"></div>

  <div class="t heading-lg" style="left:60px;top:626px">Radfographs</div>
  <div class="t opt" style="left:22px;top:643px"><span class="box"></span>Being Mafled/emafled</div>
  <div class="t opt" style="left:182px;top:643px"><span class="box"></span>Given to the Patient</div>
  <div class="t opt" style="left:342px;top:643px"><span class="box"></span>Please Take</div>
  <div class="t opt" style="left:22px;top:661px"><span class="box"></span>Other</div>
  <div class="rule" style="left:91px;top:670px;width:170px"></div>

  <div class="sheet-band"></div>
</section>

<section class="sheet sheet-back">
  <div class="t intro">You can save time by going online.Register and update your health today</div>
  <div class="tooth-chart" role="img" aria-label="Numbered adult tooth chart, teeth 1 to 32, right and left sides"></div>
  <div class="tissue-chart" role="img" aria-label="Soft tissue chart of the open mouth"></div>

  <div class="instructions-title">Patient Instructions</div>
  <p class="instructions" style="top:291px">PLEASE NOTE THAT IN MOST INSTANCES THE PATENT IS FIRST SEEN FOR CONSULATION TO REVEW THE HEALTH HISTORY; DECIDE ON THE MOST APPROPRIATE ANESTHESIAAND TREATMENT PLAN, AND SCHEDULE THE SURGERY AT A SEPARATE APPONTMENT.</p>
  <p class="instructions" style="top:354px">Please Assist us by having the following infomation avaliable with you at the time of appoint.</p>
  <p class="instructions" style="top:389px;left:21px">Ment: Your surgical referral sup and any x-rays if applicable, a list ofmedicatioins, insurance policy infomation</p>
  <p class="instructions" style="top:440px">Wportant: All patients unmarried or under the age of 19 must be accompanied by a paremt or guardian during the Consulation and Trcatment visits.</p>
  <p class="instructions" style="top:490px">SPECIAL INSTRUCTIONS FOR PATIENTS HAVING I.V SEDATOPN / GENERAL ANESTHESIA:<br>&nbsp;&nbsp;&nbsp;&nbsp;- NO FOOD OR DRINK (including Water) AT LEAST 6 HPURS [ROPR TP YPUR SURGERY UNLESS OTHERWISE INDICATED BY THE SURGEON. Some medicaitons may be continuedand this will be discussed at your consulation.</p>
  <p class="instructions" style="top:572px">&nbsp;&nbsp;&nbsp;&nbsp;. A responsible aduit must accompany you and REMAIN in the offer during the entire treatment. They must alslo be able to drive you home. YOU cannot drive until the next day.<br>&nbsp;&nbsp;&nbsp;&nbsp;&nbsp;&nbsp;.Eat a light and easily digestible meal the night before the procedure. Do not drink any alcoholife bevefages the night.before<br>&nbsp;&nbsp;&nbsp;&nbsp;&nbsp;&nbsp;.Wear comfortable clothing with sleeves which are easy to push up.</p>

  <div class="sheet-band"></div>
</section>
</body>
</html>
```